A billboard for Harlow Ridge Construction size 36.5’ x 14.5’

Hi guys. We are purchasing a billboard and are looking for a design (size 36.5’ x 14.5’). Our slogan is "Quality you deserve, service you can count on". The goal of this billboard is brand recognition primarily letting people know we do roofs. Attached are logos that can be used if needed. Not necessarily all of them need to be used.

Target Market(s)

Residents in the local areas needing or thinking about a roof replacement

Industry/Entity Type

Roofing

Requirements
Must have
• Logo and services (roof replacement, gutters, siding, and snow removal)
Nice to have
• take a look at our website for ideas www.harlowridgeconstruction.example

```html
<!DOCTYPE html>
<html lang="en">
<head>
<meta charset="utf-8">
<title>Harlow Ridge Construction Billboard</title>
<link href="https://fonts.googleapis.com/css2?family=Tinos:wght@400;700&family=Archivo+Black&family=Poppins:wght@600;700&display=swap" rel="stylesheet">
<style>
  :root {
    --ink: #000000;
    --paper: #ffffff;
    --accent-red: #d9211c;
  }
  html, body {
    margin: 0;
    padding: 0;
    width: 1200px;
    height: 1200px;
    overflow: hidden;
    background: var(--paper);
  }
  .canvas {
    position: relative;
    width: 1200px;
    height: 1200px;
  }
  .billboard {
    position: absolute;
    left: 0;
    top: 0;
    width: 1200px;
    height: 1200px;
  }
  .brand-title { font-family: "Tinos", "Times New Roman", serif; fill: var(--ink); }
  .brand-mark { font-family: "Tinos", "Times New Roman", serif; fill: var(--ink); }
  .slogan { font-family: "Archivo Black", "Arial Black", sans-serif; fill: var(--ink); }
  .services { font-family: "Tinos", "Times New Roman", serif; font-weight: 700; fill: var(--ink); }
  .footer-text { font-family: "Poppins", "Arial", sans-serif; font-weight: 700; fill: var(--paper); }
</style>
</head>
<body>
<div class="canvas">
  <svg class="billboard" viewBox="0 0 1200 1200" xmlns="http://www.w3.org/2000/svg">
    <defs>
      <linearGradient id="roofTones" x1="0" y1="0" x2="1" y2="1">
        <stop offset="0" stop-color="#a9b0a8"/>
        <stop offset="0.35" stop-color="#7a6b56"/>
        <stop offset="0.65" stop-color="#a9743c"/>
        <stop offset="1" stop-color="#5f5444"/>
      </linearGradient>
    </defs>

    <!-- frame -->
    <rect class="board-frame" x="148" y="410" width="904" height="380" fill="var(--ink)"/>
    <rect class="board-panel" x="157" y="419" width="886" height="318" fill="var(--paper)"/>

    <!-- photo area -->
    <g role="img" aria-label="Photo of a house with shingled roof gables, timber siding, arched windows and a stone chimney">
      <polygon points="157,419 402,419 540,600 422,737 157,737" fill="url(#roofTones)"/>
    </g>
    <!-- chevron edge -->
    <polygon class="chevron" points="402,419 418,419 556,600 440,737 422,737 540,600" fill="var(--ink)"/>

    <!-- title -->
    <text class="brand-title" x="488" y="496" font-size="68" textLength="350" lengthAdjust="spacingAndGlyphs">Harlow Ridge</text>
    <text class="brand-title" x="526" y="565" font-size="86" textLength="478" lengthAdjust="spacingAndGlyphs">Construction</text>

    <!-- brand name mark -->
    <rect class="mark-square" x="852" y="458" width="14" height="14" fill="var(--accent-red)"/>
    <text class="brand-mark" x="874" y="471" font-size="17">Harlow Ridge</text>
    <text class="brand-mark" x="874" y="491" font-size="17">Construction</text>

    <!-- slogan banner -->
    <polygon class="slogan-band" points="568,580 1022,580 1022,658 510,658" fill="var(--accent-red)"/>
    <text class="slogan" x="576" y="611" font-size="22" textLength="439" lengthAdjust="spacingAndGlyphs">QUALITY YOU DESERVE, SERVICE</text>
    <text class="slogan" x="556" y="645" font-size="22" textLength="372" lengthAdjust="spacingAndGlyphs">YOU CAN COUNT ON..............</text>

    <!-- services -->
    <g class="services" font-size="27">
      <circle cx="514" cy="683" r="6" fill="var(--accent-red)"/>
      <text x="524" y="692" textLength="324" lengthAdjust="spacingAndGlyphs">ROOF REPLACEMENT</text>
      <circle cx="864" cy="683" r="6" fill="var(--accent-red)"/>
      <text x="880" y="692" textLength="142" lengthAdjust="spacingAndGlyphs">GUTTERS</text>
      <circle cx="563" cy="715" r="6" fill="var(--accent-red)"/>
      <text x="577" y="724" textLength="106" lengthAdjust="spacingAndGlyphs">SIDING</text>
      <circle cx="702" cy="715" r="6" fill="var(--accent-red)"/>
      <text x="720" y="724" textLength="250" lengthAdjust="spacingAndGlyphs">SNOW REMOVAL</text>
    </g>

    <!-- footer -->
    <text class="footer-text" x="157" y="772" font-size="24" textLength="560" lengthAdjust="spacingAndGlyphs">www.harlowridgeconstruction.example</text>
    <text class="footer-text" x="766" y="771" font-size="22" textLength="279" lengthAdjust="spacing">PH: 5550193847</text>
  </svg>
</div>
</body>
</html>
```